Need a business card for auto body business

Needs to be on card:
Ridge Point Collision Marcello Verrano / Licensed Appraiser KFWR Corp Facebook Logo
418 Orchard Avenue
Alderbrook QX 02871
T 617-555-0148
F 781-555-0193
kestrelfieldworks.example
info@kestrelfieldworks.example
https://www.friendpage.example/Ridge.Point.Collision

I will attach a sample of the old Business card

Target Market(s)

Professional, business, classy,

Industry/Entity Type

Business

```html
<!DOCTYPE html>
<html lang="en">
<head>
<meta charset="utf-8">
<title>Ridge Point Collision – Business Card</title>
<link rel="stylesheet" href="https://fonts.googleapis.com/css2?family=Nunito:wght@400;600;800&display=swap">
<style>
  :root {
    --stage: #2f2f2f;
    --card-white: #f7f7f5;
    --card-grey: #9d9d9d;
    --card-grey-light: #b3b3b3;
    --brand-red: #8c0b0d;
    --brand-red-deep: #6e0709;
    --shadow-grey: #a8a8a8;
    --ink-dark: #3a3a3a;
    --ink-light: #ffffff;
  }
  * { box-sizing: border-box; margin: 0; padding: 0; }
  html, body {
    width: 1200px; height: 1000px; overflow: hidden;
    background: var(--stage);
    font-family: "Nunito", sans-serif;
  }
  .canvas { position: relative; width: 1200px; height: 1000px; }

  .card {
    position: absolute; overflow: hidden;
    box-shadow: 0 14px 30px rgba(0,0,0,.45);
  }
  .card__edge { position: absolute; top: 0; height: 100%; }

  /* Front */
  .card--front {
    left: 80px; top: 470px; width: 700px; height: 400px;
    background: var(--card-white);
  }
  .card--front .card__edge { left: 0; width: 130px; }
  .brand {
    position: absolute; left: 140px; right: 30px; top: 150px;
    text-align: center;
  }
  .brand__name {
    display: inline-flex; align-items: center; gap: 12px;
    white-space: nowrap;
    font-weight: 800; font-size: 38px; line-height: 1;
    color: var(--brand-red);
  }
  .brand__dot {
    flex: none;
    width: 20px; height: 20px; border-radius: 50%;
    background: var(--brand-red);
  }
  .brand__rule {
    width: 420px; height: 1px; margin: 22px auto 10px;
    background: var(--ink-dark);
  }
  .brand__tagline {
    font-weight: 600; font-size: 15px; letter-spacing: 4px;
    color: var(--brand-red);
  }

  /* Back */
  .card--back {
    left: 470px; top: 50px; width: 660px; height: 377px;
    background: linear-gradient(160deg, var(--card-grey-light), var(--card-grey));
  }
  .card--back .card__edge { right: 0; width: 90px; }
  .person { position: absolute; left: 56px; top: 34px; }
  .person__name {
    font-weight: 600; font-size: 30px; color: var(--brand-red);
  }
  .person__underline {
    width: 250px; height: 4px; margin: 2px 0 6px -14px;
    background: var(--brand-red); border-radius: 2px;
  }
  .person__role {
    font-size: 16px; line-height: 1.2; color: var(--brand-red-deep);
  }
  .contact {
    position: absolute; right: 110px; top: 124px;
    text-align: right; list-style: none;
    font-size: 18px; line-height: 1.38; color: var(--ink-light);
  }
  .social {
    position: absolute; left: 40px; bottom: 58px;
    display: flex; align-items: center; gap: 14px;
    white-space: nowrap;
    font-weight: 800; font-size: 16px; color: var(--ink-light);
  }
  .social__mark {
    flex: none;
    width: 26px; height: 26px; background: var(--ink-light); border-radius: 3px;
  }
</style>
</head>
<body>
<main class="canvas">

  <section class="card card--back" aria-label="Business card back">
    <svg class="card__edge" viewBox="0 0 90 377" preserveAspectRatio="none" aria-hidden="true">
      <path d="M60 0 C 20 120, 20 260, 50 377 L90 377 L90 0 Z" fill="var(--shadow-grey)"/>
      <path d="M72 0 C 34 120, 34 260, 62 377 L90 377 L90 0 Z" fill="var(--brand-red)"/>
    </svg>

    <div class="person">
      <h2 class="person__name">Marcello Verrano</h2>
      <div class="person__underline"></div>
      <p class="person__role">Licensed Appraiser<br>KFWR Corp</p>
    </div>

    <ul class="contact">
      <li>418 Orchard Avenue</li>
      <li>Alderbrook QX 02871</li>
      <li>T 617-555-0148</li>
      <li>F 781-555-0193</li>
      <li>kestrelfieldworks.example</li>
      <li>info@kestrelfieldworks.example</li>
    </ul>

    <div class="social">
      <span class="social__mark" aria-hidden="true"></span>
      <span class="social__url">https://www.friendpage.example/Ridge.Point.Collision</span>
    </div>
  </section>

  <section class="card card--front" aria-label="Business card front">
    <svg class="card__edge" viewBox="0 0 130 400" preserveAspectRatio="none" aria-hidden="true">
      <path d="M0 0 L78 0 C 110 110, 100 230, 124 400 L0 400 Z" fill="var(--shadow-grey)" opacity=".7"/>
      <path d="M0 0 L62 0 C 92 110, 82 230, 102 400 L0 400 Z" fill="var(--brand-red)"/>
    </svg>

    <div class="brand">
      <div class="brand__name">
        <span class="brand__dot" aria-hidden="true"></span>
        <span>Ridge Point Collision</span>
      </div>
      <div class="brand__rule"></div>
      <p class="brand__tagline">Expert Auto Body Repair</p>
    </div>
  </section>

</main>
</body>
</html>
```